電子書籍の表紙デザインをお願い致します。

本の内容、
冴えない20代のOLでした。そんな私でしたが約7年前に、
「たった一度きりのこの人生。もっと自分らしく、もっと輝かせたい。」
と強く熱望した瞬間があり、私は知識・人脈・実績・経験・貯金などビジネスに関してプラスになるような持ち合わせが一切ないゼロの状態で、【私らしい生き方と働き方】を一心に求めて「起業」を目指しはじめました。
今では独立を果たし、当時は未知の世界でしかなかった独立起業の道も今年で7年目に突入しました。得意な分野は、ビジネスコンサルティング、ビジネスプロデュース、コミュニティ運営、Webマーケティング、Webライティング、アフィリエイト、プロモーション、マインドコーチング、オウンドメディア構築など。写真や動画の編集・加工などクリエイティブなことも割と好きです。

私の仕事における共通点はどのビジネスでもパソコン1台とネット環境があれば場所を問わずどこでも仕事ができることです。そのライフスタイルを「スカイハーベスター」と名付け、よく国内外問わず、大好きな旅をしながら仕事をしています。

しかし、この 「起業」という働き方に出会う前の私は、好きなことをしながら仕事ができる、そんなワークスタイルがあるだなんて夢にも思っていませんでした。
そんなの理想のまた理想・・・そんなかんじで。しかしそれ以上に私が伝えたいのは、「自分でビジネスをして価値提供をする」という中で自分の思考や価値観、ライフスタイルまでも大きく変化したということなのです。そして今は毎日に充実感があり、やりがいを感じながら仕事も楽しくしています。

そして現在は、自らの経験と海外で得た感動をもとにPC1台で好きな時に・好きな場所で・好きな人と、「自分らしく、グローバルに生きていく」そんなスタイルを日々全力で、熱狂してご提供しています。

優しい雰囲気の安心できるような女性らしいカラーでお願い致します。

使って頂きたい画像と本文を添付致します。
表紙はこの4枚の画像を使って優しいイメージで、パステルカラー、薄い色を使っていただけると嬉しいです。

タイトルは
きみの毎日は花になる!扉をそっと叩いて
心ほどける日々を選び取るための小さな習慣集
でお願い致します。

はじめに、私の起業ストーリーを少しお話しさせてください。私はもともと自分に自信がまったく持てなくて、そのくせ社会不適合で、ただただ路頭に迷う、冴えない20代のOLでした。そんな私でしたが約7年前に、

日にちを19日まで延長させていただきました。
20日まで延長致しました。宜しくお願い致します。
いま、
最終段階で決定に向けて進めております。
21日で締め切らせていただきます。最後までよろしくお願いいたします。

お洒落な大人女子のイメージややんわりとしたパステルカラーの色合いがとても美しい作品だと感じました。タイトルや入れたい文字をしっかりと目立たせていただきました。自分の思い描くイメージをカタチにしてくださったなと感謝の想いでいっぱいでございます。

この度、ご提案してくださったデザイナーの皆様、最後まで吟味させて頂き、選ぶのにとても迷いました。それほど、素晴らしい作品ばかりでした。沢山のご提案を本当に有難うございました。今回はご縁を頂けなかった皆様とも、今後も定期的にコンペをさせていただく予定ですので、どうぞよろしくお願いします。

```html
<!DOCTYPE html>
<html lang="ja">
<head>
<meta charset="utf-8">
<title>心ほどける日々を選び取るための小さな習慣集</title>
<link href="https://fonts.googleapis.com/css2?family=M+PLUS+Rounded+1c:wght@500;700;800&family=Noto+Sans+JP:wght@500;700;900&display=swap" rel="stylesheet">
<style>
  :root {
    --sky: #c9e8ee;
    --teal: #1f9cad;
    --ink: #2b2b2b;
    --pink: #ea4c88;
    --pink-deep: #d63a74;
    --white: #ffffff;
    --photo-a: #b8c9a4;
    --photo-b: #d8c3a8;
    --photo-c: #e9dccb;
    --photo-d: #d9a99a;
  }
  html, body { margin: 0; padding: 0; overflow: hidden; }
  body { width: 750px; height: 1200px; background: var(--sky); }
  .cover {
    position: relative; width: 750px; height: 1200px; overflow: hidden;
    background: var(--sky);
    font-family: "M PLUS Rounded 1c", "Noto Sans JP", sans-serif;
  }
  .cover div, .cover span { white-space: nowrap; }
  .photo {
    position: absolute; border: 8px solid var(--white);
    box-shadow: 0 4px 10px rgba(0,0,0,.15);
  }
  .photo-garden { left: 14px; top: 20px; width: 215px; height: 215px; transform: rotate(-4deg);
    background: linear-gradient(160deg, #cfe3f0 0%, var(--photo-a) 60%, #8fa47a 100%); }
  .photo-group { left: 215px; top: 30px; width: 270px; height: 185px; transform: rotate(3deg);
    background: linear-gradient(170deg, #e6e2d6 0%, var(--photo-b) 55%, #9c7f66 100%); }
  .photo-terrace { left: 455px; top: -8px; width: 290px; height: 250px; transform: rotate(2deg);
    background: linear-gradient(170deg, #f1ece2 0%, var(--photo-c) 50%, #a9cfd4 100%); }

  .tagline {
    position: absolute; top: 282px; left: 0; width: 100%; text-align: center;
    color: var(--teal); font-weight: 700; font-size: 46px; letter-spacing: 2px;
  }
  .title {
    position: absolute; top: 352px; left: 0; width: 100%; margin: 0; text-align: center;
    color: var(--teal); font-weight: 800; font-size: 80px; line-height: 104px; letter-spacing: 2px;
  }
  .author { position: absolute; top: 672px; left: 0; width: 100%; text-align: center; color: var(--ink); }
  .author-role { font-size: 20px; font-weight: 500; letter-spacing: 2px; }
  .author-name { font-size: 48px; font-weight: 800; line-height: 56px; letter-spacing: 1px; }

  .band { position: absolute; left: 0; top: 762px; width: 750px; height: 318px; background: var(--pink); }
  .portrait { position: absolute; left: 0; top: 790px; width: 240px; height: 290px;
    background: linear-gradient(180deg, #f3c9d3 0%, var(--photo-d) 60%, #c4506e 100%); }
  .headline {
    position: absolute; left: 240px; right: 0; top: 790px; text-align: center;
    color: var(--white); font-family: "Noto Sans JP", sans-serif; font-weight: 900;
    font-size: 42px; line-height: 56px; letter-spacing: 1px;
  }
  .assets { position: absolute; left: 250px; right: 10px; top: 866px; display: flex; justify-content: center; gap: 10px; }
  .asset {
    background: var(--white); color: var(--pink); border-radius: 22px;
    padding: 4px 14px; font-weight: 800; font-size: 26px; line-height: 34px;
  }
  .zero {
    position: absolute; left: 290px; top: 920px; color: var(--white);
    font-weight: 800; font-size: 34px; line-height: 44px; border-bottom: 3px solid var(--white); padding-bottom: 2px;
  }
  .pc-badge {
    position: absolute; left: 246px; top: 980px; width: 90px; height: 90px; border-radius: 50%;
    background: var(--white); color: var(--pink); text-align: center;
    font-weight: 800; font-size: 24px; line-height: 28px; display: flex; align-items: center; justify-content: center;
  }
  .bubble {
    position: absolute; background: var(--white); color: var(--pink-deep);
    border-radius: 22px; padding: 2px 14px; font-weight: 800; font-size: 26px; line-height: 40px;
  }
  .bubble-time { left: 344px; top: 1028px; }
  .bubble-place { left: 472px; top: 980px; }
  .bubble-people { left: 582px; top: 1030px; }

  .footer {
    position: absolute; left: 0; top: 1080px; width: 750px; height: 120px; background: var(--white);
    display: flex; align-items: center; justify-content: center;
    color: var(--pink-deep); font-family: "Noto Sans JP", sans-serif; font-weight: 900; font-size: 37px;
  }
</style>
</head>
<body>
<div class="cover">
  <div class="photo photo-garden" role="img" aria-label="庭のベンチに座る女性の写真"></div>
  <div class="photo photo-group" role="img" aria-label="海外で子どもたちと並ぶ集合写真"></div>
  <div class="photo photo-terrace" role="img" aria-label="プールサイドのテラスで過ごす写真"></div>

  <div class="tagline">＼ 扉をそっと叩いて ／</div>
  <h1 class="title">心ほどける日々を<br>選び取るための<br>小さな習慣集</h1>

  <div class="author">
    <div class="author-role">スカイハーベスター</div>
    <div class="author-name">Hanae</div>
  </div>

  <div class="band"></div>
  <div class="portrait" role="img" aria-label="微笑む著者のポートレート写真"></div>
  <div class="headline">きみの毎日は花になる!</div>
  <div class="assets">
    <span class="asset">知識</span><span class="asset">人脈</span><span class="asset">実績</span><span class="asset">経験</span><span class="asset">貯金</span>
  </div>
  <div class="zero">すべてゼロスタートから</div>
  <div class="pc-badge">PC<br>1台で</div>
  <div class="bubble bubble-time">好きな時に、</div>
  <div class="bubble bubble-place">好きな場所で、</div>
  <div class="bubble bubble-people">好きな人と</div>

  <div class="footer">自分らしくグローバルに生きていく方法</div>
</div>
</body>
</html>
```